Kem7Dex Letterhead

Need a new letterhead for my law firm.
IDENTIFYING INFORMATION BELOW:
Ansel T Brightwater III
Attorney at Law
Address: 4832 Tillbury Rd, Ste 250, Dallas, TX 75204
Phone: 866-402-7183
Fax: 469-583-0271
Email: kem@kem7dex.example
Website: www.kem7dex.example

Colors
0054AA
0677BA
7BADD7
CADEEF
E8F1F8

Requirements
Must have
• Logo needs to be on the letterhead, along with identifying information which is included in the project description.

```html
<!DOCTYPE html>
<html lang="en">
<head>
<meta charset="utf-8">
<title>Kem7Dex Letterhead</title>
<link href="https://fonts.googleapis.com/css2?family=Arimo:wght@400;700&family=Montserrat:wght@300;400;800&display=swap" rel="stylesheet">
<style>
  :root {
    --backdrop: #b0afb0;
    --paper: #ffffff;
    --ink: #111111;
    --text: #333333;
    --muted: #8a8a8a;
    --rule: #9a9a9a;
    --brand-deep: #0054AA;
    --brand-mid: #0677BA;
    --brand-bright: #0aa0de;
    --accent-name: #1a9ad6;
    --signature-tone: #e8f1f8;
  }
  * { margin: 0; padding: 0; box-sizing: border-box; }
  html, body { width: 1200px; height: 1200px; overflow: hidden; background: var(--backdrop); }
  .sheet {
    position: absolute; left: 190px; top: 20px;
    width: 924px; height: 1306px;
    background: var(--paper);
    transform: scale(0.8874); transform-origin: 0 0;
    font-family: "Montserrat", sans-serif;
  }
  .sheet > * { position: absolute; }
  .brand-name {
    left: 60px; top: 58px;
    font-family: "Montserrat", sans-serif; font-weight: 800;
    font-size: 50px; letter-spacing: 1px; color: var(--ink);
  }
  .attorney { left: 513px; top: 52px; font-family: "Arimo", sans-serif; font-size: 15px; line-height: 18px; color: var(--text); }
  .attorney .name { color: var(--brand-mid); font-weight: 700; }
  .attorney .address { margin-top: 10px; }
  .divider-v { left: 709px; top: 54px; width: 1px; height: 80px; background: var(--rule); }
  .contacts { left: 724px; top: 52px; font-family: "Arimo", sans-serif; font-size: 15px; color: var(--text); list-style: none; }
  .contacts li { display: flex; align-items: center; height: 22px; }
  .contacts svg { width: 13px; height: 13px; margin-right: 8px; fill: var(--brand-mid); }
  .rule { left: 61px; top: 146px; width: 802px; height: 1px; background: var(--rule); }
  .salutation-to { left: 94px; top: 292px; font-size: 16px; letter-spacing: 3px; color: var(--text); }
  .date { right: 94px; top: 291px; font-size: 13px; color: var(--text); }
  .recipient { left: 94px; top: 318px; font-size: 12.5px; line-height: 20.5px; color: var(--muted); }
  .recipient .who { font-size: 16px; color: var(--accent-name); line-height: 20px; margin-bottom: 6px; }
  .body { left: 94px; top: 466px; width: 738px; font-size: 13.4px; font-weight: 300; line-height: 16.5px; color: var(--muted); text-align: justify; }
  .body p { margin-bottom: 16.3px; }
  .signature-mark { left: 94px; top: 922px; width: 160px; height: 40px; background: var(--signature-tone); border-radius: 4px; }
  .signatory { left: 92px; top: 972px; font-size: 14.5px; color: var(--text); line-height: 18px; }
  .signatory .role { font-size: 12px; color: var(--muted); }
  .footer-band { left: 0; top: 1286px; width: 924px; height: 20px; }
</style>
</head>
<body>
<div class="sheet">
  <div class="brand-name">KEM7DEX</div>

  <div class="attorney">
    <div class="name">Ansel T Brightwater III</div>
    <div>Attorney at Law</div>
    <div class="address">4832 Tillbury Rd, Ste 250<br>Dallas, TX 75204</div>
  </div>

  <div class="divider-v"></div>

  <ul class="contacts">
    <li><svg viewBox="0 0 16 16"><path d="M3 1l3 3-2 2c1 2 3 4 5 5l2-2 3 3-2 3C6 15 1 10 0 3z"/></svg>866-402-7183</li>
    <li><svg viewBox="0 0 16 16"><path d="M4 1h8v4H4zM1 6h14v7h-3v2H4v-2H1zM5 10v4h6v-4z"/></svg>469-583-0271</li>
    <li><svg viewBox="0 0 16 16"><path d="M1 3h14v10H1zM2 4l6 5 6-5v1L8 10 2 5z"/></svg>kem@kem7dex.example</li>
    <li><svg viewBox="0 0 16 16"><circle cx="8" cy="8" r="7"/></svg>www.kem7dex.example</li>
  </ul>

  <div class="rule"></div>

  <div class="salutation-to">TO</div>
  <div class="date">Friday, 01/01/2018</div>

  <div class="recipient">
    <div class="who">Dara Velenko</div>
    Human Resources<br>
    Northvale Systems<br>
    2210-B Harlow Crest, Ferndale<br>
    F42 USA
  </div>

  <div class="body">
    <p>Lorem ipsum dolor sit amet, consectetuer adipiscing elit, sed diam nonmmy nibh euismod tincidunt ut laoreet dolore magna aliquam erat volutpat. Ut wisi enim ad minim veniam, quis nostrud exerci tationmcorper suscipit lobortis nisl ut aliquip ex ea commodo consequat. Duis autem vel eum iriure dolor in hendrerit in vulputate velit esse molestie consequat, vel illum dolore eu feugiat nulla facilisis at vero eros et accumsan et iusto odio dignissim qui blandit praesent luptatum zzril delenit augue duis dolore te feugait nulla facilisi.</p>
    <p>Nam liber tempor cum soluta nobis eleifend option congue nihil imprdiet doming id quod mazim placerat facer possim assum. Typi non habent claritatem insitam;</p>
    <p>Est usus legentis in iis qui facit eorum claritatem.</p>
    <p>Investigationes demonstraverunt lectores legere me lius quod ii legunt saepius. Claritas est etiam processus dynamicus, qui sequitur mutationem consuetudium lectorum. Mirum est notare quam littera gothica, quam nunc putamus parum claram, anteposuerit litterarum formas humanitatis per seacula quarta decima et quinta decima. Eodem modo typi, qui nunc nobis videntur parum clari, fiant sollemnes in futurum.</p>
    <p>consectetuer adipiscing elit, sed diam nonummy nibh euismod tincidunt ut laoreet dolore magna aliquam erat volutpat. Ut wisi enim ad minim veniam, quis nostrud exerci tation ullamcorper suscipit lobortis nisl ut aliquip ex ea commodo consequat. Duis autem vel eum iriure dolor in hendrerit in vulputate velit esse molestie consequat, vel illum dolore eu feugiat nulla facilisis at vero eros et accumsan et iusto odio dignissim qui blandit praesent luptatum zzril delenit augue duis dolore te feugait nulla facilisi.</p>
    <p>Nam liber tempor cum soluta nobis eleifend option congue nihil imperdiet .</p>
  </div>

  <div class="signature-mark" role="img" aria-label="Handwritten signature of Owen Maddox"></div>

  <div class="signatory">
    <div>Owen Maddox</div>
    <div class="role">Managing Director</div>
  </div>

  <svg class="footer-band" viewBox="0 0 924 20" preserveAspectRatio="none" aria-hidden="true">
    <defs>
      <linearGradient id="bandBlue" x1="0" x2="1" y1="0" y2="0">
        <stop offset="0" stop-color="#0054AA"/>
        <stop offset="0.2" stop-color="#004f9c"/>
        <stop offset="0.55" stop-color="#0677BA"/>
        <stop offset="1" stop-color="#0aa0de"/>
      </linearGradient>
    </defs>
    <polygon points="0,0 648,0 630,20 0,20" fill="url(#bandBlue)"/>
    <polygon points="664,0 924,0 924,20 646,20" fill="#000"/>
  </svg>
</div>
</body>
</html>
```